Corkbell Cellars: the premier wine registry - (need business cards)

We have a logo designed, and now we need business cards for our 3 founders. Corkbell Cellars is the premier wine registry for weddings. I am envisioning the wine glass with the heart in it as our signature symbol. (FYI- on the red background file, only use the part that has the red background; the brown colors are not relevant)

```html
<!DOCTYPE html>
<html lang="en">
<head>
<meta charset="utf-8">
<title>Corkbell Cellars — Business Cards</title>
<link href="https://fonts.googleapis.com/css2?family=Montserrat:wght@400;500&display=swap" rel="stylesheet">
<style>
  :root {
    --wine: #8c1d4a;
    --wine-soft: #9a2a57;
    --silver: #c9c9cc;
    --ink-grey: #8b8b8e;
    --paper: #ffffff;
    --backdrop: #e7e7e9;
  }
  * { box-sizing: border-box; margin: 0; padding: 0; }
  html, body { width: 1200px; height: 900px; overflow: hidden; }
  body {
    background: var(--backdrop);
    font-family: "Montserrat", sans-serif;
    position: relative;
  }
  .card {
    position: absolute;
    left: 280px;
    width: 640px;
    height: 366px;
    border-radius: 28px;
    overflow: hidden;
  }
  .card--front { top: 70px; background: var(--wine); }
  .card--back { top: 470px; background: var(--paper); }

  .front-brand {
    position: absolute;
    inset: 0;
    display: flex;
    align-items: center;
    justify-content: center;
    gap: 16px;
  }
  .front-brand .brand-name {
    color: var(--silver);
    font-size: 26px;
    font-weight: 400;
    letter-spacing: 6px;
    text-transform: uppercase;
  }
  .brand-dot {
    width: 16px; height: 16px;
    border-radius: 50%;
    background: var(--silver);
  }

  .back-brand {
    position: absolute;
    top: 70px; left: 0; right: 0;
    display: flex;
    align-items: center;
    justify-content: center;
    gap: 12px;
  }
  .back-brand .brand-name {
    color: var(--wine);
    font-size: 24px;
    font-weight: 500;
    letter-spacing: 5px;
    text-transform: uppercase;
  }
  .back-brand .brand-dot { background: var(--wine); width: 14px; height: 14px; }

  .person {
    position: absolute;
    top: 148px; left: 0; right: 0;
    text-align: center;
  }
  .person-name {
    color: var(--wine);
    font-size: 22px;
    font-weight: 400;
    letter-spacing: 1px;
    text-transform: uppercase;
  }
  .person-role {
    color: var(--ink-grey);
    font-size: 15px;
    margin-top: 4px;
  }

  .details {
    position: absolute;
    top: 248px; left: 0; right: 0;
    display: flex;
    justify-content: center;
    align-items: stretch;
    gap: 16px;
    color: var(--ink-grey);
    font-size: 15px;
    line-height: 1.35;
  }
  .address { text-align: right; padding-top: 14px; }
  .divider { width: 1.5px; background: var(--ink-grey); }
  .contact { list-style: none; }
  .contact li { display: flex; align-items: center; gap: 8px; }
  .contact svg { width: 13px; height: 13px; fill: var(--wine); flex: none; }
</style>
</head>
<body>
  <section class="card card--front" aria-label="Card front">
    <div class="front-brand">
      <span class="brand-dot"></span>
      <span class="brand-name">Corkbell Cellars</span>
    </div>
  </section>

  <section class="card card--back" aria-label="Card back">
    <div class="back-brand">
      <span class="brand-dot"></span>
      <span class="brand-name">Corkbell Cellars</span>
    </div>
    <div class="person">
      <p class="person-name">Daniel Marlowe</p>
      <p class="person-role">managing director</p>
    </div>
    <div class="details">
      <address class="address" style="font-style:normal">
        48 Orchard Lane<br>
        Hillford, New York<br>
        12345
      </address>
      <span class="divider"></span>
      <ul class="contact">
        <li>
          <svg viewBox="0 0 24 24" aria-hidden="true"><path d="M6.6 10.8a15.1 15.1 0 0 0 6.6 6.6l2.2-2.2a1 1 0 0 1 1-.25 11.4 11.4 0 0 0 3.6.57 1 1 0 0 1 1 1V20a1 1 0 0 1-1 1A17 17 0 0 1 3 4a1 1 0 0 1 1-1h3.5a1 1 0 0 1 1 1c0 1.25.2 2.45.57 3.6a1 1 0 0 1-.25 1z"/></svg>
          555 555 5555
        </li>
        <li>
          <svg viewBox="0 0 24 24" aria-hidden="true"><path d="M2 5h20v14H2z" fill="none"/><path d="M2 5h20v2l-10 6L2 7zM2 9l10 6 10-6v10H2z"/></svg>
          d.marlowe@corkbellcellars.com
        </li>
        <li>
          <svg viewBox="0 0 24 24" aria-hidden="true"><path d="M12 2a10 10 0 1 0 0 20 10 10 0 0 0 0-20zm6.9 9h-3a15 15 0 0 0-1.3-5.6A8 8 0 0 1 18.9 11zM12 4.1c.9 1.2 1.8 3.6 1.9 6.9h-3.8c.1-3.3 1-5.7 1.9-6.9zM9.4 5.4A15 15 0 0 0 8.1 11h-3a8 8 0 0 1 4.3-5.6zM5.1 13h3a15 15 0 0 0 1.3 5.6A8 8 0 0 1 5.1 13zm6.9 6.9c-.9-1.2-1.8-3.6-1.9-6.9h3.8c-.1 3.3-1 5.7-1.9 6.9zm2.6-1.3a15 15 0 0 0 1.3-5.6h3a8 8 0 0 1-4.3 5.6z"/></svg>
          www.corkbellcellars.com
        </li>
      </ul>
    </div>
  </section>
</body>
</html>
```